Real Estate Sign

My company is in need of a redesign for our real estate lawn sign. The sign should show our logo, the phrase "For Sale", our phone number 410-587-3391 and website www.HomeKeelTX.com.
Updates

Hello

Thank you for your submissions.  I am looking for the website and phone number to be very visible from a good distance.  I do also want to stay within the colors of my logo. Too many colors could be expensive to reproduce.

Thank you
Gordon

I favor clean, straight lines and design.  I prefer not to add any other graphics or logos on the sign.  The logo and name are enough. I am looking for readability from a good distance and prefer calls to action like call 410-593-3391 for information or visit www.HomeKeelTX.com to schedule tour today!  I don't really need FOR SALE to be so prominent.

thanks for all the submissions.
Gordon

Gordon

Industry/Entity Type

Real Estate

```html
<!DOCTYPE html>
<html lang="en">
<head>
<meta charset="utf-8">
<title>HomeKeel Realty – Lawn Sign</title>
<link rel="stylesheet" href="https://fonts.googleapis.com/css2?family=PT+Sans:wght@400;700&display=swap">
<style>
  :root {
    --navy: #0a4a80;
    --deep: #0b4f86;
    --glow: #1c68b3;
    --sky: #41ace0;
    --white: #ffffff;
    --page: #ffffff;
  }
  * { margin: 0; padding: 0; box-sizing: border-box; }
  html, body {
    width: 1200px;
    height: 1000px;
    overflow: hidden;
    background: var(--page);
  }
  .canvas {
    position: relative;
    width: 1200px;
    height: 1000px;
    font-family: "PT Sans", "Myriad Pro", Arial, sans-serif;
    color: var(--white);
  }
  .sign {
    position: absolute;
    left: 226px;
    top: 42px;
    width: 677px;
    height: 902px;
    background: var(--navy);
  }
  .sign-frame {
    position: absolute;
    left: 10px;
    top: 10px;
    right: 13px;
    bottom: 10px;
    border: 4px solid var(--white);
  }
  .sign-panel {
    position: absolute;
    left: 15px;
    top: 15px;
    width: 645px;
    height: 718px;
    background: radial-gradient(ellipse at 50% 55%, var(--glow) 0%, var(--deep) 70%, var(--navy) 100%);
    text-align: center;
  }
  .brand {
    position: absolute;
    left: 0;
    right: 0;
    top: 88px;
    display: flex;
    justify-content: center;
    align-items: center;
    gap: 20px;
  }
  .brand-mark {
    width: 34px;
    height: 34px;
    background: var(--sky);
  }
  .brand-name {
    font-size: 74px;
    font-weight: 700;
    line-height: 1;
    color: var(--white);
    letter-spacing: 0.5px;
  }
  .call-to-action {
    position: absolute;
    left: 0;
    right: 0;
    line-height: 1;
    font-weight: 400;
  }
  .cta-tour   { top: 296px; font-size: 48px; }
  .cta-visit  { top: 372px; font-size: 48px; }
  .cta-web    { top: 446px; font-size: 54px; letter-spacing: -0.3px; }
  .cta-call   { top: 526px; font-size: 48px; }
  .cta-phone  { top: 608px; font-size: 72px; }
  .sale-band {
    position: absolute;
    left: 15px;
    top: 733px;
    width: 645px;
    height: 154px;
    background: var(--sky);
    display: flex;
    align-items: center;
    justify-content: center;
  }
  .sale-label {
    font-size: 100px;
    font-weight: 400;
    line-height: 1;
    letter-spacing: 1px;
    color: var(--white);
  }
</style>
</head>
<body>
  <main class="canvas">
    <section class="sign">
      <div class="sign-frame"></div>
      <div class="sign-panel">
        <div class="brand">
          <span class="brand-mark"></span>
          <span class="brand-name">HomeKeel Realty</span>
        </div>
        <p class="call-to-action cta-tour">To Schedule a Tour</p>
        <p class="call-to-action cta-visit">Visit</p>
        <p class="call-to-action cta-web">www.HomeKeelTX.com</p>
        <p class="call-to-action cta-call">or call</p>
        <p class="call-to-action cta-phone">410-587-3391</p>
      </div>
      <div class="sale-band">
        <span class="sale-label">FOR SALE</span>
      </div>
    </section>
  </main>
</body>
</html>
```